High End Mechanic Business Card Design Project

Automotive Business - Repair, service and sales
Bold background with clarity of text

Industry/Entity Type

Automotive

Contact Information for Business Card

Black background with silver or white kvt 418 lorne coupe at the bottom right angered with the business name and address at the top left.. Also to include a compass near the business name and the text... Sales Service RepairAdded photos as EXAMPLES. Don't want the actual n, s, e w on the compass picture but to know that it is a compass.

Font styles to use
Sans Serif

Requirements
Must have
• Creativity, black background, Images: 4 Lorne KVT Coupe & Compass (without text)

```html
<!DOCTYPE html>
<html lang="en">
<head>
<meta charset="utf-8">
<title>Halverton East Motors – Business Card</title>
<link rel="stylesheet" href="https://fonts.googleapis.com/css2?family=Saira+Semi+Condensed:wght@600&family=Saira:wght@300;400&display=swap">
<style>
  :root {
    --page: #ffffff;
    --card: #4f4f4f;
    --ink: #ffffff;
    --ink-soft: #f0f0f0;
    --accent: #1ba0e2;
    --dot: #e0262b;
    --icon: #b4b4b4;
    --mark-faint: #666666;
  }
  html, body {
    margin: 0;
    width: 1200px;
    height: 1200px;
    overflow: hidden;
    background: var(--page);
  }
  .card {
    position: absolute;
    left: 100px;
    top: 313px;
    width: 1000px;
    height: 573px;
    background: var(--card);
    border-radius: 6px;
    overflow: hidden;
  }
  .brand {
    position: absolute;
    left: 46px;
    top: 50px;
    display: flex;
    align-items: flex-start;
    gap: 14px;
  }
  .brand-name {
    margin: 0;
    font-family: "Saira Semi Condensed", sans-serif;
    font-weight: 600;
    font-size: 62px;
    line-height: 64px;
    letter-spacing: 3px;
    color: var(--ink);
    text-transform: uppercase;
  }
  .brand-dot {
    width: 18px;
    height: 18px;
    margin-top: 16px;
    border-radius: 50%;
    background: var(--accent);
  }
  .tagline {
    position: absolute;
    left: 50px;
    top: 184px;
    margin: 0;
    font-family: "Saira", sans-serif;
    font-weight: 400;
    font-size: 33px;
    letter-spacing: 1px;
    color: var(--ink-soft);
  }
  .tagline .sep {
    color: var(--dot);
    font-size: 20px;
    vertical-align: middle;
    margin: 0 10px;
  }
  .backdrop-mark {
    position: absolute;
    left: 731px;
    top: 66px;
    width: 200px;
    height: 200px;
    border-radius: 50%;
    border: 26px solid var(--mark-faint);
    box-sizing: border-box;
  }
  .contact {
    position: absolute;
    left: 50px;
    top: 412px;
    margin: 0;
    padding: 0;
    list-style: none;
    font-family: "Saira", sans-serif;
    font-weight: 300;
    font-size: 29px;
    color: var(--ink);
  }
  .contact li {
    display: flex;
    align-items: center;
    height: 40px;
  }
  .contact svg {
    width: 22px;
    height: 22px;
    margin-right: 17px;
    fill: var(--icon);
  }
  .car-photo {
    position: absolute;
    left: 508px;
    top: 356px;
    width: 466px;
    height: 185px;
    border-radius: 90px 120px 40px 40px / 70px 90px 40px 40px;
    background: radial-gradient(ellipse at 50% 40%, #d6d6d6 0%, #9a9a9a 55%, #3a3a3a 100%);
  }
</style>
</head>
<body>
  <main class="card">
    <div class="brand">
      <h1 class="brand-name">Halverton<br>East Motors</h1>
      <span class="brand-dot"></span>
    </div>
    <p class="tagline">Sales<span class="sep">●</span>Service<span class="sep">●</span>Repair</p>

    <div class="backdrop-mark" aria-hidden="true"></div>

    <ul class="contact">
      <li>
        <svg viewBox="0 0 24 24" aria-hidden="true"><path d="M12 1a8 8 0 0 0-8 8c0 6 8 14 8 14s8-8 8-14a8 8 0 0 0-8-8zm0 11a3 3 0 1 1 0-6 3 3 0 0 1 0 6z"/></svg>
        2210 Brookfield East Ave.
      </li>
      <li>
        <svg viewBox="0 0 24 24" aria-hidden="true"><path d="M12 1a8 8 0 0 0-8 8c0 6 8 14 8 14s8-8 8-14a8 8 0 0 0-8-8zm0 11a3 3 0 1 1 0-6 3 3 0 0 1 0 6z"/></svg>
        Dalton, GA 307
      </li>
      <li>
        <svg viewBox="0 0 24 24" aria-hidden="true"><path d="M2 9c0-3 4-5 10-5s10 2 10 5v2h-5V9c-1-1-3-1.5-5-1.5S8 8 7 9v2H2zM6 12h12l2 8H4zm6 1.5a3 3 0 1 0 0 6 3 3 0 0 0 0-6z"/></svg>
        555 204 7316
      </li>
    </ul>

    <div class="car-photo" role="img" aria-label="Photo of a silver KVT 4 Lorne coupe, angled three-quarter front view"></div>
  </main>
</body>
</html>
```